New Business Cards for Torvin Group

We need a new Business Card to compliment our new logo. We are a vibrant design, manufacture and install business providing recreation areas, public parks and Municipal spaces. We want business cards that are classy, modern and clean.

We have recently changed our logo, and are celebrating our 40th anniversary. We want business cards with a new modern design to reflect our status.

Target Market(s)

Customers

Contact Information for Business Card

We need all the details of our 3 offices as per the business card attached. Please disregard the old logo on the business card, the other three files show our new logo.

Requirements
Must have
• All info as per attached business card but with new logo.
Nice to have

```html
<!DOCTYPE html>
<html lang="en">
<head>
<meta charset="utf-8">
<title>Torvin Group – Business Cards</title>
<link rel="stylesheet" href="https://fonts.googleapis.com/css2?family=Open+Sans:wght@400;600;700&display=swap">
<style>
  :root {
    --backdrop: #d6d6d6;
    --charcoal: #48494b;
    --charcoal-deep: #3a3b3d;
    --red: #e3262f;
    --white: #ffffff;
    --ink: #4a4a4c;
    --muted: #6a6a6c;
  }
  * { box-sizing: border-box; margin: 0; padding: 0; }
  html, body { width: 1200px; height: 900px; overflow: hidden; }
  body {
    background: var(--backdrop);
    font-family: "Open Sans", sans-serif;
    position: relative;
  }
  .card {
    position: absolute;
    width: 620px;
    height: 354px;
    box-shadow: 0 3px 10px rgba(0,0,0,0.18);
    overflow: hidden;
  }

  /* Front */
  .card-front {
    left: 110px; top: 70px;
    background: var(--charcoal);
    display: flex; align-items: center; justify-content: center;
  }
  .front-brand { display: flex; align-items: center; gap: 18px; }
  .front-brand .brand-dot {
    width: 64px; height: 64px; border-radius: 50%;
    background: var(--charcoal-deep);
  }
  .front-brand .brand-name {
    font-size: 44px; font-weight: 700; letter-spacing: 1px;
    color: var(--charcoal-deep); text-transform: uppercase;
  }

  /* Back */
  .card-back {
    left: 470px; top: 476px;
    background: var(--white);
    display: flex;
  }
  .back-identity {
    width: 292px;
    padding: 48px 0 0 40px;
    display: flex; flex-direction: column;
  }
  .back-brand { display: flex; align-items: center; gap: 12px; }
  .back-brand .brand-dot {
    width: 52px; height: 52px; border-radius: 50%; background: var(--red);
  }
  .back-brand .brand-name {
    font-size: 27px; font-weight: 700; color: var(--ink);
    text-transform: uppercase; line-height: 1;
  }
  .back-brand .brand-est {
    display: block; font-size: 11px; font-weight: 400;
    color: var(--ink); letter-spacing: 1px; margin-top: 4px;
  }
  .person { margin-top: 40px; }
  .person-name { color: var(--red); font-size: 19px; font-weight: 600; }
  .person-role { color: var(--muted); font-size: 14px; margin-top: 2px; }
  .person-contact { margin-top: 38px; list-style: none; }
  .person-contact li {
    display: flex; align-items: center; gap: 8px;
    font-size: 14px; color: var(--muted); line-height: 1.45;
  }

  .back-offices {
    flex: 1;
    background: var(--charcoal);
    padding: 30px 0 0 26px;
    color: var(--white);
  }
  .office { margin-bottom: 13px; }
  .office-title { font-size: 13px; font-weight: 700; line-height: 1.35; }
  .office p, .office li, .office-email {
    font-size: 12.5px; line-height: 1.35; list-style: none;
  }
  .office li, .office-email { display: flex; align-items: center; gap: 7px; }

  .back-web {
    width: 34px;
    background: var(--red);
    position: relative;
  }
  .back-web span {
    position: absolute; left: 50%; top: 50%;
    transform: translate(-50%, -50%) rotate(90deg);
    color: var(--white); font-size: 13px; letter-spacing: 1.5px;
    white-space: nowrap;
  }
  .icon { width: 12px; height: 12px; flex: none; }
</style>
</head>
<body>

<section class="card card-front" aria-label="Business card front">
  <div class="front-brand">
    <span class="brand-dot"></span>
    <span class="brand-name">Torvin Group</span>
  </div>
</section>

<section class="card card-back" aria-label="Business card back">
  <div class="back-identity">
    <div class="back-brand">
      <span class="brand-dot"></span>
      <span class="brand-name">Torvin Group<span class="brand-est">EST. 1979</span></span>
    </div>
    <div class="person">
      <p class="person-name">Rami Aldous</p>
      <p class="person-role">Managing Partner</p>
    </div>
    <ul class="person-contact">
      <li>
        <svg class="icon" viewBox="0 0 12 12"><rect x="2.5" y="0.5" width="7" height="11" rx="1.2" fill="none" stroke="#e3262f"/><line x1="5" y1="9.5" x2="7" y2="9.5" stroke="#e3262f"/></svg>
        +971 (0)50 480 7712
      </li>
      <li>
        <svg class="icon" viewBox="0 0 12 12"><rect x="0.5" y="2" width="11" height="8" fill="none" stroke="#e3262f"/><path d="M0.5 2 L6 6.5 L11.5 2" fill="none" stroke="#e3262f"/></svg>
        rami@torvingroup.com
      </li>
    </ul>
  </div>

  <div class="back-offices">
    <div class="office">
      <p class="office-title">Head Office:</p>
      <p>P.O. Box: 31840 Abu Dhabi, U.A.E.</p>
      <ul>
        <li><svg class="icon" viewBox="0 0 12 12"><path d="M2.5 1 L4.5 1 L5 3.8 L3.7 4.8 Q4.8 7.2 7.2 8.3 L8.2 7 L11 7.5 L11 9.5 Q11 11 9.5 11 Q1 10 1 2.5 Q1 1 2.5 1Z" fill="#e3262f"/></svg>+971 (0)2 5530128</li>
        <li><svg class="icon" viewBox="0 0 12 12"><rect x="1" y="5" width="10" height="6" rx="1" fill="#e3262f"/><rect x="3" y="1" width="6" height="5" fill="#e3262f"/></svg>+971 (0)2 5530129</li>
      </ul>
    </div>
    <div class="office">
      <p class="office-title">Dubai Office:</p>
      <p>P.O. Box: 418206 Dubai, U.A.E.</p>
      <ul>
        <li><svg class="icon" viewBox="0 0 12 12"><path d="M2.5 1 L4.5 1 L5 3.8 L3.7 4.8 Q4.8 7.2 7.2 8.3 L8.2 7 L11 7.5 L11 9.5 Q11 11 9.5 11 Q1 10 1 2.5 Q1 1 2.5 1Z" fill="#e3262f"/></svg>+971 (0)4 3387405</li>
        <li><svg class="icon" viewBox="0 0 12 12"><rect x="1" y="5" width="10" height="6" rx="1" fill="#e3262f"/><rect x="3" y="1" width="6" height="5" fill="#e3262f"/></svg>+971 (0)4 3387406</li>
      </ul>
    </div>
    <div class="office">
      <p class="office-title">Qatar Office:</p>
      <p>P.O. Box: 22730 Doha, Qatar</p>
      <ul>
        <li><svg class="icon" viewBox="0 0 12 12"><path d="M2.5 1 L4.5 1 L5 3.8 L3.7 4.8 Q4.8 7.2 7.2 8.3 L8.2 7 L11 7.5 L11 9.5 Q11 11 9.5 11 Q1 10 1 2.5 Q1 1 2.5 1Z" fill="#e3262f"/></svg>+974 44815302</li>
        <li><svg class="icon" viewBox="0 0 12 12"><rect x="1" y="5" width="10" height="6" rx="1" fill="#e3262f"/><rect x="3" y="1" width="6" height="5" fill="#e3262f"/></svg>+974 44815390</li>
      </ul>
      <p class="office-email"><svg class="icon" viewBox="0 0 12 12"><rect x="0.5" y="2" width="11" height="8" fill="none" stroke="#e3262f"/><path d="M0.5 2 L6 6.5 L11.5 2" fill="none" stroke="#e3262f"/></svg>sales@torvingroup.com</p>
    </div>
  </div>

  <div class="back-web"><span>www.torvingroup.com</span></div>
</section>

</body>
</html>
```